Business card design incorporating discount offer

We are a trade services company and we need a double sided business card that is going to be used by our tradesmen to give to customers on completion of their jobs.

Below are the key elements of the card that we would like to include:

-Main logo with text 'Expert Property Care' underneath.
-Up to 12 smaller icon logos with text 'Your local all-trade experts' to emphasise the point that we cover all the trades
-Discount offer - 10% discount
-Telephone number and website address
-Blank space for tradesman to enter his/her name
-Request for customer feedback with feedback url

This business card will be printed on regular card. In the past we have favoured designs that use a black background but we're open to new ideas.

I have attached a few files:

-A simple wire frame example to show how this card could look with the different elements mentioned above, feel free to use a layout similar to this or come up with something totally different (biz-card.pdf)
-Front and back of a loyalty card the we've used in the past (this card was printed on plastic)
-Front and back of a key fob design that we've previously used (this card was printed on plastic)
-A logo file with the 12 small icons and the main logo image

If you need further images or information please ask.

```html
<!DOCTYPE html>
<html lang="en">
<head>
<meta charset="utf-8">
<title>Halden – Business Card</title>
<link rel="stylesheet" href="https://fonts.googleapis.com/css2?family=Arimo:wght@400;700&family=Montserrat:wght@700;800&display=swap">
<style>
  :root {
    --stage: #d3d4d5;
    --card-dark: #343234;
    --card-light: #ffffff;
    --accent-blue: #2b7cc6;
    --ink: #2e2c2e;
    --tile-wood: #b98250;
    --tile-violet: #b04fa5;
    --tile-amber: #d9a42b;
    --tile-slate: #6f7d8a;
    --tile-grey: #8d8f92;
    --tile-sky: #1f8fdc;
    --tile-yellow: #e5c93a;
    --tile-teal: #2fb3b7;
    --tile-red: #d8343d;
    --tile-green: #6cb347;
  }
  * { box-sizing: border-box; margin: 0; padding: 0; }
  html, body { width: 1200px; height: 1000px; overflow: hidden; }
  body { background: var(--stage); position: relative; font-family: "Arimo", Arial, sans-serif; }

  .card { position: absolute; width: 665px; height: 410px; display: flex; box-shadow: 0 12px 28px rgba(0,0,0,.18); }
  .card--front { left: 75px; top: 100px; }
  .card--back { left: 470px; top: 530px; }

  /* Front */
  .front-brand { flex: 0 0 450px; background: var(--card-dark); color: #fff; position: relative; }
  .brand-name { position: absolute; left: 92px; top: 112px; font-weight: 700; font-size: 62px; letter-spacing: 1px; }
  .brand-tagline { position: absolute; left: 75px; top: 222px; font-weight: 700; font-size: 31px; }
  .contact { position: absolute; left: 84px; top: 328px; font-weight: 700; font-size: 27px; line-height: 32px; }
  .contact-row { display: flex; align-items: center; gap: 8px; }
  .contact-row svg { width: 24px; height: 24px; flex: none; }

  .front-offer { flex: 1; background: var(--card-light); color: var(--ink); position: relative; }
  .offer-figure { position: absolute; left: 34px; top: 78px; font-family: "Montserrat", Arial, sans-serif; font-weight: 800; font-size: 96px; line-height: 1; color: var(--accent-blue); letter-spacing: -3px; }
  .offer-figure sup { font-size: 30px; position: absolute; top: -10px; right: -26px; letter-spacing: 0; }
  .offer-label { position: absolute; left: 34px; top: 196px; font-family: "Montserrat", Arial, sans-serif; font-weight: 800; font-size: 25px; }
  .offer-note { position: absolute; left: 42px; top: 224px; font-size: 21px; }
  .offer-terms { position: absolute; left: 36px; top: 340px; font-size: 14.5px; line-height: 18px; }

  /* Back */
  .back-trades { flex: 0 0 205px; background: var(--card-light); display: grid; grid-template-columns: repeat(2, 62px); grid-auto-rows: 62px; gap: 10px 14px; align-content: center; justify-content: center; }
  .trade-tile { border-radius: 10px; box-shadow: inset 0 -4px 0 rgba(0,0,0,.18), 0 2px 3px rgba(0,0,0,.25); }
  .trade-tile--carpentry { background: var(--tile-wood); }
  .trade-tile--bathrooms { background: var(--tile-violet); }
  .trade-tile--joinery { background: var(--tile-amber); }
  .trade-tile--plumbing { background: var(--tile-slate); }
  .trade-tile--electrics { background: var(--tile-grey); }
  .trade-tile--gas { background: var(--tile-sky); }
  .trade-tile--heating { background: var(--tile-yellow); }
  .trade-tile--appliances { background: var(--tile-teal); }
  .trade-tile--decorating { background: var(--tile-red); }
  .trade-tile--pest { background: var(--tile-green); }

  .back-info { flex: 1; background: var(--card-dark); color: #fff; position: relative; }
  .back-headline { position: absolute; left: 8px; top: 34px; font-weight: 700; font-size: 25px; display: flex; align-items: center; gap: 6px; }
  .back-headline svg { width: 20px; height: 16px; }
  .tradesman-label { position: absolute; left: 38px; top: 112px; font-size: 20px; }
  .tradesman-field { position: absolute; left: 38px; top: 140px; width: 375px; height: 82px; background: #fff; }
  .feedback-title { position: absolute; left: 50px; top: 280px; font-weight: 700; font-size: 19.5px; }
  .feedback-text { position: absolute; left: 54px; top: 330px; font-size: 19.5px; line-height: 22px; }
  .feedback-text strong { font-weight: 700; }
</style>
</head>
<body>

<section class="card card--front" aria-label="Card front">
  <div class="front-brand">
    <div class="brand-name">Halden</div>
    <div class="brand-tagline">Expert Property Care</div>
    <div class="contact">
      <div class="contact-row">
        <svg viewBox="0 0 24 24" aria-hidden="true"><rect width="24" height="24" rx="2" fill="#fff"/><path d="M7 4l3 1 1 4-2 1.5c1 2.5 3 4.5 5.5 5.5L16 14l4 1 1 3-2 2C12 20 4 12 4 6z" fill="#343234"/></svg>
        <span>0800 555 0142</span>
      </div>
      <div class="contact-row">
        <svg viewBox="0 0 24 24" aria-hidden="true"><rect width="24" height="24" rx="2" fill="#fff"/><g fill="none" stroke="#343234" stroke-width="1.4"><circle cx="12" cy="12" r="8"/><ellipse cx="12" cy="12" rx="3.5" ry="8"/><path d="M4 12h16M5.5 8h13M5.5 16h13"/></g></svg>
        <span>haldenhome.co.uk</span>
      </div>
    </div>
  </div>
  <div class="front-offer">
    <div class="offer-figure">10<sup>%</sup></div>
    <div class="offer-label">DISCOUNT</div>
    <div class="offer-note">with this card</div>
    <div class="offer-terms">Check our website for<br>full Offer Details</div>
  </div>
</section>

<section class="card card--back" aria-label="Card back">
  <div class="back-trades">
    <div class="trade-tile trade-tile--carpentry" role="img" aria-label="Hammer icon for carpentry"></div>
    <div class="trade-tile trade-tile--bathrooms" role="img" aria-label="Bathtub icon for bathrooms"></div>
    <div class="trade-tile trade-tile--joinery" role="img" aria-label="Saw icon for joinery"></div>
    <div class="trade-tile trade-tile--plumbing" role="img" aria-label="Pipe icon for plumbing"></div>
    <div class="trade-tile trade-tile--electrics" role="img" aria-label="Lightning icon for electrics"></div>
    <div class="trade-tile trade-tile--gas" role="img" aria-label="Flame icon for gas"></div>
    <div class="trade-tile trade-tile--heating" role="img" aria-label="Tools icon for maintenance"></div>
    <div class="trade-tile trade-tile--appliances" role="img" aria-label="Oven icon for appliances"></div>
    <div class="trade-tile trade-tile--decorating" role="img" aria-label="Paintbrush icon for decorating"></div>
    <div class="trade-tile trade-tile--pest" role="img" aria-label="Insect icon for pest control"></div>
  </div>
  <div class="back-info">
    <div class="back-headline">
      <svg viewBox="0 0 20 16" aria-hidden="true"><path d="M9 2L3 8l6 6M16 2l-6 6 6 6" fill="none" stroke="#fff" stroke-width="2.4"/></svg>
      <span>Your Local All-Trade Experts</span>
    </div>
    <div class="tradesman-label">Your Halden Tradesman:</div>
    <div class="tradesman-field"></div>
    <div class="feedback-title">What Do You Think of Our Services?</div>
    <div class="feedback-text">Please leave your feedback online:<br><strong>www.haldenhome.co.uk/feedback</strong></div>
  </div>
</section>

</body>
</html>
```